Financial Advisor / Asset Manager Zup Design

I'm currently hosting with Zup and my first attempt at a website is live at www.ravenholtwealth.example Clearly I am not a web designer and I need help making this more catchy, modern, cross-platform compatible, search engine optimized, etc. I've got logos, hex color pallets, and a slew of other graphics. I'm interested in working with a winning designer to write/refine my copy/language to complete the build.

Full set of graphics https://pics.lumora-share.example/q71TzR05KwPd2MhXN do NOT use the CONSULTING graphics as this is for a related business / different website

Target Market(s)

Individuals, small institutions, endowments, non-profits seeking financial advice and asset / portfolio management

Industry/Entity Type

Financial Services

Coding

Coded - Design and coding required

Font styles to use
Other font styles liked:
• AvenirLTStd - Black, Book, and Roman as appropriate

Requirements
Must have
• Complete, cross platform website integrating my existing logo
Nice to have
• Easy to update format for go-forward maintenance

```html
<!DOCTYPE html>
<html lang="en">
<head>
<meta charset="utf-8">
<title>Ravenholt Wealth — Personalized Financial Advice</title>
<link href="https://fonts.googleapis.com/css2?family=Nunito+Sans:wght@400;600;700;800;900&display=swap" rel="stylesheet">
<style>
:root{
  --sky:#0aa3ea;
  --navy:#0a4ea3;
  --ink:#14213a;
  --text:#3b4250;
  --muted:#6b7280;
  --line:#cfd8e3;
  --footer:#16202e;
  --white:#ffffff;
}
*{box-sizing:border-box;margin:0;padding:0}
html,body{width:1200px;height:4539px;overflow:hidden}
body{position:relative;font-family:"Nunito Sans",Arial,sans-serif;color:var(--text);background:var(--white)}
.abs{position:absolute}
a{color:inherit;text-decoration:none}

/* header */
.site-header{left:0;top:0;width:1200px;height:127px;background:var(--white)}
.brand{left:92px;top:56px;font-weight:800;font-size:24px;color:var(--sky);display:flex;align-items:center;gap:8px}
.brand .dot{width:18px;height:18px;border-radius:50%;background:var(--sky)}
.welcome{left:600px;top:14px;font-size:15px;color:var(--text);border-left:2px solid var(--navy);padding-left:6px}
.callbar{left:872px;top:0;width:328px;height:49px;background:var(--navy);color:var(--white);font-size:15px;display:flex;align-items:center;padding-left:60px}
.callbar b{margin-left:5px}
.callbar .ico{position:absolute;left:14px;top:8px;width:34px;height:34px}
.nav{top:78px;font-size:16px;color:var(--text)}
.nav.active{color:var(--navy);font-weight:700}

/* hero */
.hero{left:0;top:127px;width:1200px;height:557px;background:linear-gradient(180deg,#6d8fb3 0%,#b9c7d4 30%,#3f5a3a 55%,#1e2d2a 70%,#5c6d72 100%)}
.hero-title{left:90px;top:165px;font-weight:900;font-size:64px;line-height:66px;color:var(--white)}
.hero-title span{color:var(--sky)}
.hero-sub{left:93px;top:311px;font-size:20px;letter-spacing:5px;font-weight:700;color:var(--white)}
.btn{display:flex;align-items:center;justify-content:center;gap:12px;color:var(--white);font-weight:700;font-size:18px;border-bottom:3px solid var(--navy)}
.btn .arr{width:20px;height:20px}
.btn-sky{background:var(--sky)}
.btn-navy{background:var(--navy);border-bottom-color:var(--sky)}
.hero-btn{left:93px;top:490px;width:192px;height:53px}
.slide-arrow{top:361px;width:32px;height:79px;background:rgba(20,40,70,.75);display:flex;align-items:center;justify-content:center}
.hero-arrow-r{background:var(--navy)}

/* values */
.value{width:238px;height:238px;border-radius:50%;background:var(--navy);color:var(--white);text-align:center;padding:70px 22px 0}
.value h3{font-size:18px;font-weight:800}
.value h3::after{content:"";display:block;width:40px;height:2px;background:var(--sky);margin:10px auto 12px}
.value p{font-size:15px;line-height:28px}
.value.photo{background:linear-gradient(160deg,#5a5f66,#2b3038 60%,#3b4048)}
.value-ring{width:262px;height:262px}

/* about */
.about-mark{left:92px;top:1128px;width:390px;height:380px;display:flex;flex-direction:column;align-items:center;justify-content:center;gap:14px}
.about-mark .dot{width:60px;height:60px;border-radius:50%;background:var(--sky)}
.about-mark span{font-weight:800;font-size:34px;color:var(--navy)}
.h2{font-weight:800;font-size:38px;color:var(--ink)}
.h2::after{content:"";display:block;width:30px;height:3px;background:var(--sky);margin-top:10px}
.h2.center::after{margin:10px auto 0}
.body-copy{font-size:17px;line-height:31.5px;color:var(--text)}

/* offers */
.offers{left:0;top:1612px;width:1200px;height:684px;background:var(--sky)}
.offers-cut{left:0;top:2254px;width:1200px;height:50px}
.offer-card{top:1801px;width:490px;height:317px;background:var(--white);padding:30px 28px}
.offer-card .icon{position:absolute;left:28px;top:24px;width:90px;height:90px}
.offer-card h3{position:absolute;left:158px;top:58px;font-size:20px;font-weight:800;color:var(--ink)}
.offer-card p{position:absolute;left:28px;top:150px;right:36px;font-size:16px;line-height:31.5px;color:var(--text)}
.offer-card .more{position:absolute;left:28px;top:262px;font-size:17px;color:var(--navy);display:flex;gap:10px;align-items:center}
.offer-card .corner{position:absolute;right:-8px;top:-8px;width:36px;height:36px}
.circle-arrow{top:1930px;width:56px;height:56px;border:2px solid rgba(255,255,255,.8);border-radius:50%;display:flex;align-items:center;justify-content:center}

/* philanthropy */
.phil-photo{left:654px;top:2389px;width:453px;height:398px;background:linear-gradient(180deg,#9eb0c4 0%,#6e7c88 35%,#2e3d2c 65%,#5f7177 85%,#8a9ba4 100%)}
.bar{height:4px;background:var(--sky)}

/* contact */
.contact{left:0;top:2900px;width:1200px;height:540px;background:linear-gradient(180deg,#ffffff 0%,#f3f5f7 40%,#d9dee3 75%,#c5ccd2 100%)}
.c-ico{width:48px;height:48px;border-radius:50%;background:var(--sky);display:flex;align-items:center;justify-content:center}
.c-line{font-size:17px;line-height:29px;color:var(--text);border-left:3px solid var(--navy);padding-left:12px}
.field{background:rgba(255,255,255,.9);border:2px solid #2aa8ea;font-size:15px;color:var(--muted);padding:14px 16px}
.submit{left:944px;top:3311px;width:163px;height:49px}

/* faq */
.faq-open{left:92px;top:3633px;width:496px;height:328px;border:2px solid #2aa8ea;padding:20px}
.faq-q{display:flex;align-items:center;gap:14px;font-size:16px;color:var(--ink);font-weight:600}
.faq-q .pm{margin-left:auto;font-size:22px;font-weight:400}
.faq-open p{font-size:16px;line-height:31.5px;color:var(--text);margin-top:26px}
.faq-item{left:610px;width:497px;height:49px;border:2px solid #2aa8ea;padding:0 20px;display:flex}

/* footer */
.footer{left:0;top:4132px;width:1200px;height:407px;background:var(--footer)}
.f-h{font-size:18px;font-weight:800;color:var(--white)}
.f-h::after{content:"";display:block;width:30px;height:2px;background:var(--white);margin-top:8px}
.f-link{font-size:16px;color:#e5e8ee;line-height:31.8px}
.f-brand{left:904px;top:4290px;font-weight:800;font-size:28px;color:var(--sky);display:flex;align-items:center;gap:10px}
.f-brand .dot{width:22px;height:22px;border-radius:50%;background:var(--sky)}
.copy{left:92px;top:4494px;font-size:15px;color:#b6bcc7}
.social{left:1063px;top:4483px;width:40px;height:40px;border-radius:50%;background:#3a4350}
</style>
</head>
<body>

<!-- header -->
<header class="site-header abs"></header>
<a class="brand abs" href="#"><span class="dot"></span>Ravenholt Wealth</a>
<div class="welcome abs">Welcome to Ravenholt Wealth</div>
<div class="callbar abs">
  <svg class="ico" viewBox="0 0 34 34"><path d="M11 8l4 5-2 3c1.5 3 3.5 5 6 6l3-2 5 4-2 3c-9 0-17-8-17-17z" fill="none" stroke="#fff" stroke-width="2"/></svg>
  Call Us: <b>(555) 014-2280</b>
</div>
<nav>
  <a class="nav abs active" style="left:637px">Home</a>
  <a class="nav abs" style="left:734px">About</a>
  <a class="nav abs" style="left:831px">Services ▾</a>
  <a class="nav abs" style="left:959px">FAQs</a>
  <a class="nav abs" style="left:1048px">Contact</a>
</nav>

<!-- hero -->
<section class="hero abs" role="img" aria-label="Photograph of snowy mountains reflected in a forest-lined lake"></section>
<h1 class="hero-title abs">Personalized<br>Financial <span>Advice</span></h1>
<div class="hero-sub abs">TO HELP YOU ACHIEVE YOUR GOALS</div>
<a class="btn btn-sky hero-btn abs" href="#">Contact Us <svg class="arr" viewBox="0 0 20 20"><circle cx="10" cy="10" r="9" fill="#fff"/><path d="M6 10h7M10 6.5l3.5 3.5-3.5 3.5" stroke="#0aa3ea" stroke-width="2" fill="none"/></svg></a>
<div class="slide-arrow abs" style="left:0"><svg width="10" height="16" viewBox="0 0 10 16"><path d="M8 2L2 8l6 6" stroke="#fff" stroke-width="2" fill="none"/></svg></div>
<div class="slide-arrow hero-arrow-r abs" style="left:1168px"><svg width="10" height="16" viewBox="0 0 10 16"><path d="M2 2l6 6-6 6" stroke="#fff" stroke-width="2" fill="none"/></svg></div>
<svg class="abs" style="left:0;top:630px" width="1200" height="60" viewBox="0 0 1200 60"><path d="M1130 54 Q1170 30 1200 20 V60 H0 V54 Z" fill="#fff"/><path d="M1120 54 Q1160 34 1200 22 V14 Q1160 26 1130 54 Z" fill="#0a4ea3"/></svg>

<!-- values -->
<svg class="abs" style="left:0;top:755px" width="1200" height="140" viewBox="0 0 1200 140">
  <g fill="none" stroke="#0aa3ea" stroke-width="3">
    <path d="M103 130 A131 131 0 0 1 365 130"/>
    <path d="M346 130 A131 131 0 0 1 608 130"/>
    <path d="M587 130 A131 131 0 0 1 849 130"/>
    <path d="M830 130 A131 131 0 0 1 1092 130"/>
  </g>
</svg>
<div class="value abs" style="left:115px;top:780px"><h3>You Come First</h3><p>We always act in the best interests of our clients</p></div>
<div class="value photo abs" style="left:358px;top:780px" role="img" aria-label="Photograph of advisors meeting with a client"><h3>Personalized Services</h3><p>We get to know you in order to service your unique needs</p></div>
<div class="value abs" style="left:599px;top:780px"><h3>Transparent Fees</h3><p>You'll always know what you pay and how we get paid</p></div>
<div class="value abs" style="left:842px;top:780px"><h3>We Give Back</h3><p>We support and better our local communities</p></div>

<!-- about -->
<div class="about-mark abs"><div class="dot"></div><span>Ravenholt Wealth</span></div>
<h2 class="h2 abs" style="left:583px;top:1138px">Who We Are</h2>
<p class="body-copy abs" style="left:583px;top:1216px;width:520px">Ravenholt Wealth is an investment advisory firm committed to serving as fiduciary to our clients. We always act in the best interests of our clients, including putting your interests ahead of our own. We provide independent financial planning, investment management, and asset management services tailored to your unique needs and circumstances.</p>
<a class="btn btn-sky abs" style="left:584px;top:1436px;width:192px;height:53px" href="#">Read More <svg class="arr" viewBox="0 0 20 20"><circle cx="10" cy="10" r="9" fill="#fff"/><path d="M6 10h7M10 6.5l3.5 3.5-3.5 3.5" stroke="#0aa3ea" stroke-width="2" fill="none"/></svg></a>

<!-- offers -->
<section class="offers abs"></section>
<svg class="offers-cut abs" viewBox="0 0 1200 50" preserveAspectRatio="none"><path d="M0 0 H1200 V42 H70 L0 50 Z" fill="#0aa3ea"/><path d="M0 20 L70 42 L0 50 Z" fill="#0a4ea3"/></svg>
<h2 class="h2 center abs" style="left:0;top:1688px;width:1200px;text-align:center;color:#fff">What We Offer</h2>
<div class="circle-arrow abs" style="left:18px"><svg width="10" height="16" viewBox="0 0 10 16"><path d="M8 2L2 8l6 6" stroke="#fff" stroke-width="2" fill="none"/></svg></div>
<div class="circle-arrow abs" style="left:1125px"><svg width="10" height="16" viewBox="0 0 10 16"><path d="M2 2l6 6-6 6" stroke="#fff" stroke-width="2" fill="none"/></svg></div>

<article class="offer-card abs" style="left:92px">
  <svg class="corner" viewBox="0 0 36 36"><path d="M4 4h28v28" fill="none" stroke="#8fd4f5" stroke-width="3"/></svg>
  <svg class="icon" viewBox="0 0 90 90"><path d="M45 2 83 24v42L45 88 7 66V24z" fill="#e8f4fc"/><g fill="none" stroke="#0a4ea3" stroke-width="2"><rect x="26" y="26" width="38" height="40"/><circle cx="38" cy="38" r="7"/><path d="M50 60V48M56 60V42M44 60V52"/></g></svg>
  <h3>Financial Planning</h3>
  <p>You and your circumstances are unique. We want to work to meet you where you are today, and help you get to where you want to be in the future.</p>
  <a class="more" href="#">Read More <svg width="20" height="20" viewBox="0 0 20 20"><circle cx="10" cy="10" r="9" fill="#0a4ea3"/><path d="M6 10h7M10 6.5l3.5 3.5-3.5 3.5" stroke="#fff" stroke-width="2" fill="none"/></svg></a>
</article>
<article class="offer-card abs" style="left:617px">
  <svg class="corner" viewBox="0 0 36 36"><path d="M4 4h28v28" fill="none" stroke="#8fd4f5" stroke-width="3"/></svg>
  <svg class="icon" viewBox="0 0 90 90"><path d="M45 2 83 24v42L45 88 7 66V24z" fill="#e8f4fc"/><g fill="none" stroke="#0a4ea3" stroke-width="2"><rect x="34" y="24" width="32" height="30"/><path d="M40 48v-8M47 48V34M54 48v-11M61 48v-16"/><path d="M22 66c8-8 16-8 22-4h10"/></g></svg>
  <h3>Asset Management</h3>
  <p>Many advisors use a screening process to find investments. You may be familiar with stock screening as many websites and investment platforms</p>
  <a class="more" href="#">Read More <svg width="20" height="20" viewBox="0 0 20 20"><circle cx="10" cy="10" r="9" fill="#0a4ea3"/><path d="M6 10h7M10 6.5l3.5 3.5-3.5 3.5" stroke="#fff" stroke-width="2" fill="none"/></svg></a>
</article>
<a class="btn btn-navy abs" style="left:506px;top:2162px;width:190px;height:51px" href="#">View More <svg class="arr" viewBox="0 0 20 20"><circle cx="10" cy="10" r="9" fill="#fff"/><path d="M6 10h7M10 6.5l3.5 3.5-3.5 3.5" stroke="#0a4ea3" stroke-width="2" fill="none"/></svg></a>

<!-- philanthropy -->
<h2 class="h2 abs" style="left:92px;top:2398px">Your Philanthropy</h2>
<p class="body-copy abs" style="left:92px;top:2475px;width:515px">Ravenholt Wealth was founded with a purpose to make comprehensive and sophisticated financial services available to more investors. In addition to our unwavering commitment to our clients, we are dedicated to supporting and bettering our local communities. We contribute a percentage of net profits to charitable organizations each year and donate our time and services to those in need.</p>
<a class="btn btn-sky abs" style="left:93px;top:2725px;width:192px;height:53px" href="#">Contact Us <svg class="arr" viewBox="0 0 20 20"><circle cx="10" cy="10" r="9" fill="#fff"/><path d="M6 10h7M10 6.5l3.5 3.5-3.5 3.5" stroke="#0aa3ea" stroke-width="2" fill="none"/></svg></a>
<div class="phil-photo abs" role="img" aria-label="Photograph of a forested mountain above a calm lake"></div>
<div class="bar abs" style="left:942px;top:2799px;width:124px"></div>
<div class="bar abs" style="left:1072px;top:2799px;width:14px"></div>
<div class="bar abs" style="left:1092px;top:2799px;width:15px"></div>

<!-- contact -->
<section class="contact abs" role="img" aria-label="Faint background photograph of a misty lake and forest"></section>
<h2 class="h2 abs" style="left:92px;top:2952px">Contact Us</h2>
<p class="body-copy abs" style="left:92px;top:3030px;width:410px">Ravenholt Wealth was founded with a purpose to make comprehensive and sophisticated</p>
<div class="c-ico abs" style="left:92px;top:3135px"><svg width="22" height="22" viewBox="0 0 22 22"><path d="M11 20s7-7 7-11a7 7 0 0 0-14 0c0 4 7 11 7 11z" fill="none" stroke="#fff" stroke-width="2"/><circle cx="11" cy="9" r="2.5" fill="#fff"/></svg></div>
<div class="c-line abs" style="left:154px;top:3127px">1280 Alder Mill Rd, Suite #40<br>Brookhaven, VT 05099</div>
<div class="abs" style="left:92px;top:3208px;width:276px;height:1px;background:var(--line)"></div>
<div class="c-ico abs" style="left:92px;top:3236px"><svg width="22" height="22" viewBox="0 0 22 22"><path d="M6 3l4 5-2 3c1.5 3 3.5 5 6 6l3-2 4 4-2 3C10 22 0 12 0 3z" transform="translate(1 -1) scale(.9)" fill="none" stroke="#fff" stroke-width="2"/></svg></div>
<div class="c-line abs" style="left:154px;top:3228px">Call Us:<br>(555) 014-2280</div>

<h2 class="h2 abs" style="left:581px;top:2952px">Get In Touch</h2>
<div class="field abs" style="left:581px;top:3039px;width:256px;height:50px">First Name *</div>
<div class="field abs" style="left:849px;top:3039px;width:258px;height:50px">Last Name *</div>
<div class="field abs" style="left:581px;top:3105px;width:256px;height:50px">Email *</div>
<div class="field abs" style="left:849px;top:3105px;width:258px;height:50px">Phone No *</div>
<div class="field abs" style="left:581px;top:3168px;width:526px;height:127px">Leave us a message *</div>
<a class="btn btn-sky submit abs" href="#">Submit <svg class="arr" viewBox="0 0 20 20"><circle cx="10" cy="10" r="9" fill="#fff"/><path d="M6 10h7M10 6.5l3.5 3.5-3.5 3.5" stroke="#0aa3ea" stroke-width="2" fill="none"/></svg></a>

<!-- faq -->
<h2 class="h2 center abs" style="left:0;top:3512px;width:1200px;text-align:center">Frequently Asked Questions</h2>
<div class="faq-open abs">
  <div class="faq-q"><svg width="18" height="18" viewBox="0 0 20 20"><circle cx="10" cy="10" r="9" fill="#0a4ea3"/><path d="M6 10h7M10 6.5l3.5 3.5-3.5 3.5" stroke="#fff" stroke-width="2" fill="none"/></svg>What is a fiduciary? Are you a fiduciary?<span class="pm">–</span></div>
  <p>Yes, Ravenholt Wealth is a fiduciary. As a fiduciary, we are legally and ethically bound to act in the best interests of our clients. We put our clients' interests ahead of all else, including ahead of the company's and our own personal interests.<br>This is important because not all financial institutions or financial advisors are fiduciaries.</p>
</div>
<div class="faq-item faq-q abs" style="top:3637px"><svg width="18" height="18" viewBox="0 0 20 20"><circle cx="10" cy="10" r="9" fill="#0a4ea3"/><path d="M6 10h7M10 6.5l3.5 3.5-3.5 3.5" stroke="#fff" stroke-width="2" fill="none"/></svg>What is a custodian? Are you a custodian?<span class="pm">+</span></div>
<div class="faq-item faq-q abs" style="top:3705px"><svg width="18" height="18" viewBox="0 0 20 20"><circle cx="10" cy="10" r="9" fill="#0a4ea3"/><path d="M6 10h7M10 6.5l3.5 3.5-3.5 3.5" stroke="#fff" stroke-width="2" fill="none"/></svg>What are your fees? How much will I pay?<span class="pm">+</span></div>
<div class="faq-item faq-q abs" style="top:3774px"><svg width="18" height="18" viewBox="0 0 20 20"><circle cx="10" cy="10" r="9" fill="#0a4ea3"/><path d="M6 10h7M10 6.5l3.5 3.5-3.5 3.5" stroke="#fff" stroke-width="2" fill="none"/></svg>How will you keep me informed?<span class="pm">+</span></div>
<div class="faq-item faq-q abs" style="top:3843px"><svg width="18" height="18" viewBox="0 0 20 20"><circle cx="10" cy="10" r="9" fill="#0a4ea3"/><path d="M6 10h7M10 6.5l3.5 3.5-3.5 3.5" stroke="#fff" stroke-width="2" fill="none"/></svg>Are you a registered investment advisor?<span class="pm">+</span></div>
<div class="faq-item faq-q abs" style="top:3912px"><svg width="18" height="18" viewBox="0 0 20 20"><circle cx="10" cy="10" r="9" fill="#0a4ea3"/><path d="M6 10h7M10 6.5l3.5 3.5-3.5 3.5" stroke="#fff" stroke-width="2" fill="none"/></svg>Why does it matter?<span class="pm">+</span></div>
<a class="btn btn-sky abs" style="left:506px;top:4007px;width:190px;height:51px" href="#">Read More <svg class="arr" viewBox="0 0 20 20"><circle cx="10" cy="10" r="9" fill="#fff"/><path d="M6 10h7M10 6.5l3.5 3.5-3.5 3.5" stroke="#0aa3ea" stroke-width="2" fill="none"/></svg></a>

<!-- footer -->
<footer class="footer abs"></footer>
<svg class="abs" style="left:0;top:4126px" width="1200" height="50" viewBox="0 0 1200 50"><path d="M0 0 H1200 V50 H0 Z" fill="#16202e"/><path d="M0 0 H1200 V8 H70 L0 50 Z" fill="#fff"/><path d="M0 38 L70 8 H1200 V26 H80 L0 50 Z" fill="#0a4ea3"/></svg>
<div class="f-h abs" style="left:92px;top:4218px">Quick Links</div>
<div class="abs" style="left:92px;top:4266px">
  <div class="f-link">Home</div><div class="f-link">About</div><div class="f-link">FAQs</div><div class="f-link">Contact</div>
</div>
<div class="f-h abs" style="left:301px;top:4218px">Our Services</div>
<div class="abs" style="left:301px;top:4266px">
  <div class="f-link">Financial Planning</div><div class="f-link">Asset Management</div><div class="f-link">Portfolio Optimization</div><div class="f-link">Alternative Investments</div>
</div>
<div class="f-h abs" style="left:574px;top:4218px">Contact Info</div>
<svg class="abs" style="left:576px;top:4272px" width="22" height="26" viewBox="0 0 22 26"><path d="M11 24s8-8 8-13a8 8 0 0 0-16 0c0 5 8 13 8 13z" fill="none" stroke="#0aa3ea" stroke-width="2"/><circle cx="11" cy="11" r="3" fill="none" stroke="#0aa3ea" stroke-width="2"/></svg>
<div class="f-link abs" style="left:614px;top:4266px">1280 Alder Mill Rd, Suite #40<br>Brookhaven, VT 05099</div>
<svg class="abs" style="left:576px;top:4351px" width="24" height="18" viewBox="0 0 24 18"><rect x="1" y="1" width="22" height="16" rx="2" fill="none" stroke="#0aa3ea" stroke-width="2"/><path d="M2 2l10 8 10-8" fill="none" stroke="#0aa3ea" stroke-width="2"/></svg>
<div class="f-link abs" style="left:614px;top:4345px">info@ravenholtwealth.example</div>
<div class="f-brand abs"><span class="dot"></span>Ravenholt Wealth</div>
<div class="abs" style="left:0;top:4468px;width:1200px;height:1px;background:#2c3646"></div>
<div class="copy abs">Copyright © 2022 Ravenholt Wealth. All Rights Reserved.</div>
<div class="social abs" aria-label="Social profile"></div>

</body>
</html>
```